Business Card Design

We need a new buisness card designed for a new company in Darwin
We dig trenchs and lay pipes for the communication industry,Electrical industry, Teleco industry,
We also do some concrete works as well,
And small excavation work
Communication
Belvanti Contracting PTY LTD
Pit and Pipe installations
Trenching,Excavations, Concreting ,
civil works, unistrut soloutions ,over thirty years experiance
WHERE NOT FAZED WE WILL LAY ANYTHING
Contact Glen 0491536208 ps
(would like name to stand out somehow in another text or graphic sort of a way am also looking for some sort of slogan) will most likely be a red card with black writing

```html
<!DOCTYPE html>
<html lang="en">
<head>
<meta charset="utf-8">
<title>Belvanti Contracting PTY LTD – Business Card</title>
<link rel="stylesheet" href="https://fonts.googleapis.com/css2?family=Tinos&family=Dancing+Script:wght@500&family=Open+Sans:ital,wght@1,500&family=Questrial&display=swap">
<style>
  :root {
    --card-red: #e03a50;
    --brick-shadow: #c92d43;
    --ink: #111111;
  }
  html, body {
    margin: 0;
    padding: 0;
    width: 1200px;
    height: 740px;
    overflow: hidden;
    background: var(--card-red);
  }
  .card {
    position: relative;
    width: 1200px;
    height: 740px;
    overflow: hidden;
    color: var(--ink);
  }
  .brick-texture {
    position: absolute;
    inset: 0;
    width: 1200px;
    height: 740px;
  }
  .company-name {
    position: absolute;
    left: 0;
    right: 0;
    top: 48px;
    margin: 0;
    text-align: center;
    font-family: "Tinos", serif;
    font-weight: 400;
    font-size: 74px;
    line-height: 1;
    transform: scaleX(0.86);
  }
  .slogan {
    position: absolute;
    left: 0;
    right: 0;
    top: 186px;
    margin: 0;
    padding-left: 30px;
    text-align: center;
    font-family: "Dancing Script", cursive;
    font-weight: 500;
    font-size: 54px;
    line-height: 1;
    letter-spacing: 2px;
    transform: skewX(-8deg);
  }
  .services {
    position: absolute;
    left: 174px;
    top: 300px;
    margin: 0;
    padding: 0;
    list-style: none;
    font-family: "Open Sans", sans-serif;
    font-style: italic;
    font-weight: 500;
    font-size: 31px;
    line-height: 49px;
  }
  .contact {
    position: absolute;
    left: 542px;
    top: 592px;
    display: flex;
    align-items: baseline;
    white-space: nowrap;
  }
  .contact-label {
    font-family: "Questrial", sans-serif;
    font-size: 33px;
    letter-spacing: 1px;
    margin-right: 26px;
  }
  .contact-name {
    font-family: "Tinos", serif;
    font-size: 82px;
    line-height: 1;
    display: inline-block;
    transform: scaleX(0.9);
    transform-origin: left;
    margin-right: 18px;
  }
  .contact-phone {
    font-family: "Tinos", serif;
    font-size: 30px;
    letter-spacing: 1px;
  }
</style>
</head>
<body>
  <div class="card">
    <svg class="brick-texture" role="img" aria-label="Red brick wall texture background" viewBox="0 0 1200 740">
      <rect width="1200" height="740" fill="var(--card-red)"/>
    </svg>

    <h1 class="company-name">Belvanti Contracting PTY LTD</h1>
    <p class="slogan">We do it professionaly</p>

    <ul class="services">
      <li>*&nbsp; Pit and Pipe installation Specialist’s</li>
      <li>* Trenching</li>
      <li>* Excavations</li>
      <li>* Concreting.</li>
    </ul>

    <div class="contact">
      <span class="contact-label">Contact :</span>
      <span class="contact-name">Glen</span>
      <span class="contact-phone">0491536208</span>
    </div>
  </div>
</body>
</html>
```